Social Health & Parkinson's

I need a 1-pg horizontal infographic that can be handed out to patients and providers. It needs to be scientifically sound (data provided), easy to understand, and visually pleasing. Target audience; patiens (mostly 40-90 years old) and providers (neurologists, nurses, physical therapists, naturopathic physicians, support group leaders, etc.) We need 6 of these, one for each topic listed on the website. Ideally, we'll hire the winner for 5 more similar projects and keep a theme.

Target Market(s)

Patients with Parkinson's disease, their families, care providers. To be handed out by physicians, support group leaders, etc.

Colors

Designer to choose colors to be used in the design.

Requirements
Must have
• Visually stunning. Data integrity-- keep the numbers and the figures we provide. Reference to where the data is coming from. Be thoughtful of elderly, vision issues. Teach everyone something.

```html
<!DOCTYPE html>
<html lang="en">
<head>
<meta charset="utf-8">
<title>Social Health &amp; Patient-Reported Outcomes in PD</title>
<link href="https://fonts.googleapis.com/css2?family=Roboto:wght@400;500;700&family=Roboto+Condensed:wght@400;500;700&family=Montserrat:wght@400;500;700&display=swap" rel="stylesheet">
<style>
:root{
  --navy:#163c7a;
  --sky:#2f7fc1;
  --rule:#4fa6cc;
  --tab:#2a78c8;
  --tab-dark:#1b5aa0;
  --tab-light:#4a9de3;
  --tab-light-dark:#2c7cc6;
  --ink:#222;
  --body:#6a6a6a;
  --panel:#fff;
}
*{margin:0;padding:0;box-sizing:border-box}
html,body{width:1200px;height:848px;overflow:hidden;background:#fff}
.poster{position:relative;width:1200px;height:848px;background:#fff;font-family:"Roboto",sans-serif;color:var(--ink)}
.masthead-title{position:absolute;left:42px;top:15px;font:700 40.5px/1 "Roboto",sans-serif;color:var(--navy);letter-spacing:-.3px;white-space:nowrap}
.masthead-sub{position:absolute;left:42px;top:67px;font:700 27px/1 "Roboto",sans-serif;color:var(--sky);white-space:nowrap}
.partner-dot{position:absolute;top:12px;width:78px;height:78px;border-radius:50%}
.partner-dot.crimson{left:992px;background:#8c1d1d}
.partner-dot.violet{left:1091px;background:#6a55d6}
.partner-name{position:absolute;top:97px;width:110px;text-align:center;font:700 9px/1 "Roboto",sans-serif;color:var(--navy)}
.rule{position:absolute;left:0;width:1200px;height:5px;background:var(--rule)}
.field{position:absolute;left:0;top:119px;width:1200px;height:679px;background:linear-gradient(180deg,#e2e3e5,#f3f3f4 60%,#ececed)}
.card{position:absolute;background:var(--panel);box-shadow:0 1px 3px rgba(0,0,0,.18)}
.card svg{display:block;width:100%;height:100%}
.tab{position:absolute;display:flex;align-items:center;justify-content:center;text-align:center;z-index:3}
.tab::before{content:"";position:absolute;left:-15px;right:-15px;top:0;bottom:7px;background:var(--tab-dark);clip-path:polygon(15px 0,calc(100% - 15px) 0,100% 100%,0 100%);z-index:0}
.tab::after{content:"";position:absolute;inset:0;background:var(--tab);z-index:1}
.tab.light::before{background:var(--tab-light-dark)}
.tab.light::after{background:var(--tab-light)}
.tab span{position:relative;z-index:2;color:#fff;font:700 8.3px/1.3 "Montserrat",sans-serif;text-transform:uppercase;white-space:nowrap}
.tab.feature::before{left:-19px;right:-19px;bottom:5px;clip-path:polygon(19px 0,calc(100% - 19px) 0,100% 100%,0 100%)}
.tab.feature span{font:700 24px/25px "Roboto Condensed",sans-serif}
.findings{position:absolute;left:410px;width:410px;font:400 15px/18.8px "Roboto Condensed",sans-serif;color:var(--body);text-align:justify;text-align-last:center}
.takeaway{position:absolute;left:363px;width:474px;top:665px;text-align:center;font:500 20.5px/21px "Roboto Condensed",sans-serif;color:var(--sky)}
.band{position:absolute;left:0;top:737px;width:1200px;height:48px;background:linear-gradient(90deg,#ededed,#e1e1e1 50%,#ededed);display:flex;align-items:center;justify-content:center;text-align:center;font:400 15.4px/20px "Montserrat",sans-serif;color:var(--ink)}
.footer{position:absolute;left:0;top:803px;width:1200px;height:45px}
.footer-link,.footer-credit{position:absolute;top:16px;font:500 15.5px/1 "Montserrat",sans-serif;letter-spacing:1.6px;color:#444}
.footer-link{left:34px}
.footer-credit{right:34px}
svg text{font-family:"Roboto",sans-serif}
</style>
</head>
<body>
<main class="poster">
  <header>
    <h1 class="masthead-title">Social Health &amp; Patient-Reported Outcomes in PD</h1>
    <p class="masthead-sub">Rx: Nurture social health. Make friends. Avoid loneliness.</p>
    <span class="partner-dot crimson"></span><span class="partner-name" style="left:976px">Northfield University</span>
    <span class="partner-dot violet"></span><span class="partner-name" style="left:1075px">Steady Steps</span>
  </header>
  <div class="rule" style="top:114px"></div>
  <div class="field"></div>

  <svg width="0" height="0" style="position:absolute">
    <defs>
      <pattern id="scatterBlue" width="18" height="12" patternUnits="userSpaceOnUse">
        <g fill="#3a6fd0"><circle cx="2" cy="2" r="1.4"/><circle cx="6" cy="1" r="1.4"/><circle cx="10" cy="3" r="1.4"/><circle cx="14" cy="1.5" r="1.4"/><circle cx="17" cy="4" r="1.4"/><circle cx="3" cy="6" r="1.4"/><circle cx="8" cy="5.5" r="1.4"/><circle cx="12" cy="7" r="1.4"/><circle cx="16" cy="8" r="1.4"/><circle cx="1" cy="10" r="1.4"/><circle cx="5" cy="9.5" r="1.4"/><circle cx="9" cy="11" r="1.4"/><circle cx="13" cy="10.5" r="1.4"/><circle cx="17" cy="11.5" r="1.4"/></g>
      </pattern>
      <pattern id="scatterOlive" width="20" height="14" patternUnits="userSpaceOnUse">
        <g fill="#6f8a22"><circle cx="3" cy="2" r="1.1"/><circle cx="11" cy="5" r="1.1"/><circle cx="17" cy="1" r="1.1"/><circle cx="6" cy="9" r="1.1"/><circle cx="14" cy="11" r="1.1"/><circle cx="19" cy="8" r="1.1"/></g>
      </pattern>
      <pattern id="scatterGreen" width="10" height="8" patternUnits="userSpaceOnUse">
        <g fill="#3d7a1c"><circle cx="2" cy="2" r="1.2"/><circle cx="6" cy="1" r="1.2"/><circle cx="8.5" cy="5" r="1.2"/><circle cx="3" cy="6" r="1.2"/><circle cx="5.5" cy="4" r="1.2"/></g>
      </pattern>
    </defs>
  </svg>

  <!-- Left column -->
  <div class="tab" style="left:58px;top:135px;width:232px;height:37px"><span>Correlation between quality of life<br>and PRO-PD score</span></div>
  <section class="card" style="left:22px;top:165px;width:305px;height:152px">
    <svg viewBox="0 0 305 152">
      <rect x="16" y="14" width="13" height="116" fill="#ececec"/>
      <text transform="translate(26,96) rotate(-90)" font-size="7.5" font-weight="700" fill="#333">PRO-PD Score</text>
      <rect x="50" y="14" width="224" height="46" fill="#f9c49a"/>
      <rect x="50" y="60" width="224" height="23" fill="#fbdcc6"/>
      <rect x="50" y="83" width="224" height="24" fill="#bccbe8"/>
      <rect x="50" y="107" width="224" height="23" fill="#d3ecd0"/>
      <polygon points="50,50 52,14 80,20 120,35 170,50 210,75 205,120 180,130 50,130" fill="url(#scatterOlive)"/>
      <polygon points="50,130 50,55 62,45 80,62 100,95 118,130" fill="url(#scatterGreen)"/>
      <g fill="#6f8a22"><circle cx="128" cy="22" r="1"/><circle cx="150" cy="30" r="1"/><circle cx="186" cy="62" r="1"/><circle cx="196" cy="40" r="1"/><circle cx="200" cy="92" r="1"/><circle cx="188" cy="112" r="1"/><circle cx="160" cy="104" r="1"/><circle cx="140" cy="118" r="1"/><circle cx="205" cy="25" r="1"/><circle cx="175" cy="20" r="1"/><circle cx="212" cy="58" r="1"/><circle cx="126" cy="98" r="1"/></g>
      <rect x="216" y="14" width="14" height="116" fill="#d8d8d8"/>
      <text transform="translate(226,96) rotate(-90)" font-size="7.5" font-weight="700" fill="#333">Quality of Life</text>
      <line x1="50" y1="107" x2="243" y2="52" stroke="#4a6bb0" stroke-width="1"/>
      <g font-size="8" fill="#333" font-weight="500" text-anchor="middle"><text x="251" y="35">Poor</text><text x="251" y="73">Fair</text><text x="251" y="97">Good</text><text x="251" y="121">Excellent</text></g>
      <g font-size="5.5" fill="#333">
        <g text-anchor="end"><text x="46" y="132">0</text><text x="46" y="109">500</text><text x="46" y="86">1000</text><text x="46" y="63">1500</text><text x="46" y="40">2000</text><text x="46" y="17">2500</text></g>
        <g text-anchor="middle"><text x="83" y="139">5</text><text x="115" y="139">10</text><text x="147" y="139">15</text><text x="178" y="139">20</text><text x="210" y="139">25</text><text x="242" y="139">30</text><text x="274" y="139">35</text>
        <text x="162" y="147" font-size="6">Years Since Diagnosis</text></g>
      </g>
    </svg>
  </section>

  <div class="tab light" style="left:58px;top:333px;width:232px;height:37px"><span>In general, please rate how well you<br>rate your satisfaction with your social<br>activities and relationships</span></div>
  <section class="card" style="left:22px;top:364px;width:305px;height:150px">
    <svg viewBox="0 0 305 150">
      <line x1="66" y1="16" x2="66" y2="101" stroke="#777" stroke-width=".6"/>
      <line x1="66" y1="101" x2="265" y2="101" stroke="#777" stroke-width=".6"/>
      <g font-size="5.5" font-weight="700" fill="#222" text-anchor="end"><text x="62" y="103">0</text><text x="62" y="82">500</text><text x="62" y="61">1000</text><text x="62" y="40">1500</text><text x="62" y="18">2000</text></g>
      <text transform="translate(42,70) rotate(-90)" font-size="6.5" font-weight="700" fill="#222">PRO-PD</text>
      <rect x="72" y="80" width="26" height="21" fill="#c9540f"/><rect x="112" y="72.7" width="26" height="28.3" fill="#b5316c"/><rect x="153" y="63.2" width="25" height="37.8" fill="#4e7f2a"/><rect x="195" y="51" width="24" height="50" fill="#3a8a72"/><rect x="235" y="45" width="24" height="56" fill="#2a6bb0"/>
      <g font-size="6" fill="#333" text-anchor="middle"><text x="85" y="76">494</text><text x="125" y="69">667</text><text x="165" y="59">889</text><text x="207" y="47">1178</text><text x="247" y="41">1317</text></g>
      <g font-size="5.5" font-weight="700" fill="#222" text-anchor="end">
        <text transform="translate(96,108) rotate(-35)">Excellent (n=343)</text><text transform="translate(136,108) rotate(-35)">Very Good (n=607)</text><text transform="translate(176,108) rotate(-35)">Good (n=468)</text><text transform="translate(217,108) rotate(-35)">Fair (n=289)</text><text transform="translate(257,108) rotate(-35)">Poor (n=61)</text>
      </g>
      <text x="162" y="145" font-size="6.5" font-weight="700" fill="#222" text-anchor="middle">Social Satisfaction</text>
    </svg>
  </section>

  <div class="tab light" style="left:58px;top:533px;width:232px;height:38px"><span>In general, please rate how well<br>you carry out your social<br>activities and roles</span></div>
  <section class="card" style="left:22px;top:563px;width:305px;height:152px">
    <svg viewBox="0 0 305 152">
      <line x1="66" y1="15" x2="66" y2="106" stroke="#777" stroke-width=".6"/>
      <line x1="66" y1="106" x2="265" y2="106" stroke="#777" stroke-width=".6"/>
      <g font-size="5.5" font-weight="700" fill="#222" text-anchor="end"><text x="62" y="108">0</text><text x="62" y="85">500</text><text x="62" y="63">1000</text><text x="62" y="40">1500</text><text x="62" y="17">2000</text></g>
      <text transform="translate(42,72) rotate(-90)" font-size="6.5" font-weight="700" fill="#222">PRO-PD</text>
      <rect x="72" y="85.7" width="25" height="20.3" fill="#c9540f"/><rect x="112" y="76.3" width="23" height="29.7" fill="#b5316c"/><rect x="152" y="64" width="23" height="42" fill="#4e7f2a"/><rect x="191" y="49.9" width="23" height="56.1" fill="#3a8a72"/><rect x="230" y="39.4" width="23" height="66.6" fill="#2a6bb0"/>
      <g font-size="6" fill="#333" text-anchor="middle"><text x="84" y="81">446</text><text x="123" y="72">653</text><text x="163" y="60">922</text><text x="202" y="46">1233</text><text x="241" y="35">1464</text></g>
      <g font-size="5.5" font-weight="700" fill="#222" text-anchor="end">
        <text transform="translate(94,113) rotate(-35)">Excellent (n=322)</text><text transform="translate(133,113) rotate(-35)">Very Good (n=647)</text><text transform="translate(173,113) rotate(-35)">Good (n=491)</text><text transform="translate(212,113) rotate(-35)">Fair (n=247)</text><text transform="translate(251,113) rotate(-35)">Poor (n=44)</text>
      </g>
      <text x="158" y="147" font-size="6.5" font-weight="700" fill="#222" text-anchor="middle">Social Performance</text>
    </svg>
  </section>

  <!-- Centre column -->
  <div class="tab feature" style="left:393px;top:145px;width:417px;height:64px"><span>MODIFIABLE VARIABLES ASSOCIATED<br>WITH RISK OF PARKINSONS DISEASE</span></div>
  <section class="card" style="left:363px;top:204px;width:474px;height:446px">
    <svg viewBox="0 0 474 257" style="height:257px">
      <g stroke="#ddd" stroke-width=".6">
        <line x1="112" y1="16" x2="112" y2="212"/><line x1="154.3" y1="16" x2="154.3" y2="212"/><line x1="196.5" y1="16" x2="196.5" y2="212"/><line x1="238.8" y1="16" x2="238.8" y2="212"/><line x1="281" y1="16" x2="281" y2="212"/><line x1="323.3" y1="16" x2="323.3" y2="212"/><line x1="365.5" y1="16" x2="365.5" y2="212"/><line x1="407.8" y1="16" x2="407.8" y2="212"/><line x1="450" y1="16" x2="450" y2="212"/>
      </g>
      <g fill="#2c47c0">
        <rect x="153.7" y="20.5" width="127.3" height="5"/><rect x="157.5" y="38.6" width="123.5" height="5"/><rect x="180.8" y="56.7" width="100.2" height="5"/><rect x="184.1" y="74.8" width="96.9" height="5"/><rect x="199.8" y="92.9" width="81.2" height="5"/><rect x="210" y="111" width="71" height="5"/><rect x="219.3" y="129.1" width="61.7" height="5"/><rect x="260.7" y="147.2" width="20.3" height="5"/><rect x="281" y="165.3" width="58.8" height="5"/><rect x="281" y="183.4" width="76.1" height="5"/><rect x="281" y="201.5" width="138.7" height="5"/>
      </g>
      <g font-size="5.8" fill="#444" text-anchor="end">
        <text x="105" y="25">Exercise 30+ min/d, 7 days/ wk</text><text x="105" y="43">Exercise 30+ min/d, 6 days/ wk</text><text x="105" y="61">Exercise 30+ min/d, 5 days/ wk</text><text x="105" y="79">Exercise 30+ min/d, 4 days/ wk</text><text x="105" y="97">Exercise 30+ min/d, 3 days/ wk</text><text x="105" y="115">I have lots of friends</text><text x="105" y="133">I cook most of my meals</text><text x="105" y="151">I practice stress management</text><text x="105" y="170">I am overweight</text><text x="105" y="188">I have a lot of stress</text><text x="105" y="206">I am lonely</text>
        <text x="150" y="25">-301</text><text x="154" y="43">-292</text><text x="177" y="61">-237</text><text x="181" y="79">-229</text><text x="196" y="97">-192</text><text x="206" y="115">-168</text><text x="216" y="133">-146</text><text x="257" y="151">-48</text>
      </g>
      <g font-size="5.8" fill="#444"><text x="343" y="170">139</text><text x="361" y="188">180</text><text x="423" y="206">328</text></g>
      <g font-size="5.8" fill="#444" text-anchor="middle"><text x="112" y="223">-400</text><text x="154.3" y="223">-300</text><text x="196.5" y="223">-200</text><text x="238.8" y="223">-100</text><text x="281" y="223">0</text><text x="323.3" y="223">100</text><text x="365.5" y="223">200</text><text x="407.8" y="223">300</text><text x="450" y="223">400</text></g>
    </svg>
    <div style="position:absolute;left:0;top:257px;width:474px;height:1px;background:#555"></div>
  </section>
  <p class="findings" style="top:469px">Individuals who reported feeling lonely reported greater overall PD symptom severity (+328; p=0.000), which was even higher than scores for smoking tobacco (+173; p=0.005) and having a lot of stress (+180; p=0.000).</p>
  <p class="findings" style="top:555px">In contrast, individuals that reported having a lot of friends had reduced PD severity scores (-168; p=0.000). Notably, exercising 7 days per week was less beneficial (301; p=0.000) than feeling lonely was detrimental.</p>
  <p class="takeaway">Overall, individuals identifying as being lonely<br>reported consistently greater PD symptom severity.</p>

  <!-- Right column -->
  <div class="tab" style="left:908px;top:135px;width:232px;height:37px"><span>Quality of life vs. tremor</span></div>
  <section class="card" style="left:873px;top:165px;width:305px;height:152px">
    <svg viewBox="0 0 305 152">
      <g stroke="#e2e2e2" stroke-width=".5">
        <line x1="39.5" y1="5" x2="286.5" y2="5"/><line x1="39.5" y1="25" x2="286.5" y2="25"/><line x1="39.5" y1="45" x2="286.5" y2="45"/><line x1="39.5" y1="65" x2="286.5" y2="65"/><line x1="39.5" y1="85" x2="286.5" y2="85"/><line x1="39.5" y1="105" x2="286.5" y2="105"/><line x1="39.5" y1="125" x2="286.5" y2="125"/>
        <line x1="39.5" y1="5" x2="39.5" y2="125"/><line x1="88.9" y1="5" x2="88.9" y2="125"/><line x1="138.3" y1="5" x2="138.3" y2="125"/><line x1="187.7" y1="5" x2="187.7" y2="125"/><line x1="237.1" y1="5" x2="237.1" y2="125"/><line x1="286.5" y1="5" x2="286.5" y2="125"/>
      </g>
      <polygon points="40,25 105,24 150,25 200,28 230,42 252,55 256,70 240,80 205,84 170,88 130,84 95,82 60,80 40,78" fill="url(#scatterBlue)"/>
      <g fill="#3a6fd0"><circle cx="56" cy="96" r="1.4"/><circle cx="62" cy="101" r="1.4"/><circle cx="72" cy="92" r="1.4"/><circle cx="94" cy="104" r="1.4"/><circle cx="108" cy="94" r="1.4"/><circle cx="118" cy="90" r="1.4"/><circle cx="150" cy="96" r="1.4"/><circle cx="165" cy="100" r="1.4"/><circle cx="185" cy="92" r="1.4"/><circle cx="205" cy="95" r="1.4"/><circle cx="225" cy="90" r="1.4"/><circle cx="260" cy="40" r="1.4"/><circle cx="268" cy="52" r="1.4"/><circle cx="274" cy="44" r="1.4"/><circle cx="286" cy="44" r="1.4"/><circle cx="280" cy="70" r="1.4"/><circle cx="262" cy="84" r="1.4"/><circle cx="272" cy="78" r="1.4"/><circle cx="258" cy="62" r="1.4"/><circle cx="255" cy="96" r="1.4"/><circle cx="243" cy="73" r="1.4"/><circle cx="176" cy="18" r="1.4"/><circle cx="200" cy="20" r="1.4"/><circle cx="220" cy="28" r="1.4"/><circle cx="240" cy="36" r="1.4"/></g>
      <line x1="39.5" y1="48" x2="286.5" y2="65" stroke="#d23a3a" stroke-width="1" stroke-dasharray="1.5 1.5"/>
      <text x="241" y="19" font-size="6" fill="#444">R² = 0.0754</text>
      <g font-size="6" fill="#444" text-anchor="end"><text x="34" y="127">0</text><text x="34" y="107">10</text><text x="34" y="87">20</text><text x="34" y="67">30</text><text x="34" y="47">40</text><text x="34" y="27">50</text><text x="34" y="7">60</text></g>
      <g font-size="6" fill="#444" text-anchor="middle"><text x="39.5" y="134">0</text><text x="88.9" y="134">20</text><text x="138.3" y="134">40</text><text x="187.7" y="134">60</text><text x="237.1" y="134">80</text><text x="286.5" y="134">100</text><text x="163" y="146" font-size="7">Tremor</text></g>
      <text transform="translate(19,120) rotate(-90)" font-size="6.5" fill="#444">PROMIS Total - Quality of Life</text>
    </svg>
  </section>

  <div class="tab light" style="left:908px;top:333px;width:232px;height:37px"><span>Quality of life vs. withdrawn</span></div>
  <section class="card" style="left:873px;top:364px;width:305px;height:150px">
    <svg viewBox="0 0 305 150">
      <g stroke="#e2e2e2" stroke-width=".5">
        <line x1="42.6" y1="11" x2="277" y2="11"/><line x1="42.6" y1="29.8" x2="277" y2="29.8"/><line x1="42.6" y1="48.6" x2="277" y2="48.6"/><line x1="42.6" y1="67.4" x2="277" y2="67.4"/><line x1="42.6" y1="86.2" x2="277" y2="86.2"/><line x1="42.6" y1="105" x2="277" y2="105"/><line x1="42.6" y1="124" x2="277" y2="124"/>
        <line x1="42.6" y1="11" x2="42.6" y2="124"/><line x1="89.5" y1="11" x2="89.5" y2="124"/><line x1="136.4" y1="11" x2="136.4" y2="124"/><line x1="183.2" y1="11" x2="183.2" y2="124"/><line x1="230.1" y1="11" x2="230.1" y2="124"/><line x1="277" y1="11" x2="277" y2="124"/>
      </g>
      <polygon points="43,30 70,30 100,36 130,40 170,44 210,54 234,60 238,84 215,90 180,84 140,78 100,74 70,70 43,66" fill="url(#scatterBlue)"/>
      <g fill="#3a6fd0"><circle cx="50" cy="76" r="1.4"/><circle cx="56" cy="84" r="1.4"/><circle cx="72" cy="80" r="1.4"/><circle cx="94" cy="84" r="1.4"/><circle cx="100" cy="90" r="1.4"/><circle cx="126" cy="86" r="1.4"/><circle cx="150" cy="90" r="1.4"/><circle cx="172" cy="92" r="1.4"/><circle cx="196" cy="96" r="1.4"/><circle cx="240" cy="80" r="1.4"/><circle cx="244" cy="92" r="1.4"/><circle cx="248" cy="100" r="1.4"/><circle cx="256" cy="94" r="1.4"/><circle cx="264" cy="98" r="1.4"/><circle cx="276" cy="90" r="1.4"/><circle cx="276" cy="72" r="1.4"/><circle cx="242" cy="104" r="1.4"/><circle cx="134" cy="32" r="1.4"/><circle cx="160" cy="36" r="1.4"/><circle cx="198" cy="42" r="1.4"/><circle cx="224" cy="48" r="1.4"/><circle cx="236" cy="66" r="1.4"/></g>
      <line x1="42.6" y1="47" x2="277" y2="86.5" stroke="#d23a3a" stroke-width="1" stroke-dasharray="1.5 1.5"/>
      <text x="235" y="25" font-size="6" fill="#444">R² = 0.4872</text>
      <g font-size="6" fill="#444" text-anchor="end"><text x="36" y="126">0</text><text x="36" y="107">10</text><text x="36" y="89">20</text><text x="36" y="70">30</text><text x="36" y="51">40</text><text x="36" y="32">50</text><text x="36" y="13">60</text></g>
      <g font-size="6" fill="#444" text-anchor="middle"><text x="42.6" y="134">0</text><text x="89.5" y="134">20</text><text x="136.4" y="134">40</text><text x="183.2" y="134">60</text><text x="230.1" y="134">80</text><text x="277" y="134">100</text><text x="160" y="145" font-size="7">Withdrawn</text></g>
      <text transform="translate(22,120) rotate(-90)" font-size="6.5" fill="#444">PROMIS Total - Quality of Life</text>
    </svg>
  </section>

  <div class="tab light" style="left:908px;top:533px;width:232px;height:38px"><span>Average PRO-PD by years<br>since diagnosis</span></div>
  <section class="card" style="left:873px;top:563px;width:305px;height:152px">
    <svg viewBox="0 0 305 152">
      <line x1="62" y1="127" x2="255" y2="127" stroke="#ccc" stroke-width=".5"/>
      <g font-size="4.5" fill="#333" text-anchor="end"><text x="58" y="129">0</text><text x="58" y="112">200</text><text x="58" y="94">400</text><text x="58" y="77">600</text><text x="58" y="60">800</text><text x="58" y="42">1000</text><text x="58" y="25">1200</text></g>
      <text transform="translate(43,86) rotate(-90)" font-size="4.5" font-weight="700" fill="#333">PRO-PD</text>
      <polyline points="71,43.6 88.5,50.5 106,43.4 123.5,46.4 141,35.6 158.5,24.6 176,13.8 193.5,24.6 211,36.5 228.5,12.5 246,11.6" fill="none" stroke="#ef8a2c" stroke-width="1.2"/>
      <polyline points="71,80.2 88.5,73.5 106,74.7 123.5,67.9 141,69 158.5,67 176,56.9 193.5,52.5 211,49.3 228.5,44.8 246,42.4" fill="none" stroke="#3a6fc4" stroke-width="1.2"/>
      <g font-size="4" fill="#333">
        <text x="73" y="42">961</text><text x="89" y="56">881</text><text x="106" y="41">963</text><text x="124" y="52">928</text><text x="141" y="33">1053</text><text x="159" y="22">1180</text><text x="172" y="11">1304</text><text x="193" y="30">1180</text><text x="211" y="42">1043</text><text x="222" y="10">1319</text><text x="244" y="9">1330</text>
        <text x="71" y="86">539</text><text x="87" y="79">616</text><text x="105" y="80">603</text><text x="123" y="73">681</text><text x="140" y="74">668</text><text x="157" y="72">691</text><text x="175" y="62">808</text><text x="192" y="58">858</text><text x="209" y="55">895</text><text x="227" y="49">947</text><text x="249" y="43">975</text>
      </g>
      <g font-size="4.5" fill="#333" text-anchor="middle"><text x="71" y="134">0</text><text x="88.5" y="134">1</text><text x="106" y="134">2</text><text x="123.5" y="134">3</text><text x="141" y="134">4</text><text x="158.5" y="134">5</text><text x="176" y="134">6</text><text x="193.5" y="134">7</text><text x="211" y="134">8</text><text x="228.5" y="134">9</text><text x="246" y="134">10</text><text x="151" y="141" font-weight="700">Years Since Diagnosis</text></g>
      <line x1="122" y1="147" x2="132" y2="147" stroke="#ef8a2c" stroke-width="1"/><text x="133" y="148.5" font-size="4.5" fill="#333">LONELY</text>
      <line x1="152" y1="147" x2="162" y2="147" stroke="#3a6fc4" stroke-width="1"/><text x="163" y="148.5" font-size="4.5" fill="#333">NOT LONELY</text>
    </svg>
  </section>

  <p class="band">Although tremor is a cardinal symptom of PD and highly visible, feeling socially withdrawn is more closely correlated to<br>overall quality of life than tremor.</p>
  <div class="rule" style="top:798px"></div>
  <footer class="footer">
    <span class="footer-link">www.SteadyStepsPD.org</span>
    <span class="footer-credit">2020 R. Halvorsen</span>
  </footer>
</main>
</body>
</html>
```